integrative health clinic-Medical massage, acupuncture, chiropractic

we like our logo, but are open to new ideas. We need a new card design. We have added chiropractic and acupuncture that we have put under the name of the business. We are an integrative medical clinic

Target Market(s)

General public, athletes

Contact Information for Business Card

Phone 5055583927
Fax 5055583926
Hours Monday-Friday 9-6
Saturday 10-6
The 20% can be smaller on the back

Colors
3176b5
0355a3

Requirements
Must have
• Logo but am open to ideas
Nice to have
• We are an integrated medical clinic but also want to be personable. We want the card fun and inviting

```html
<!DOCTYPE html>
<html lang="en">
<head>
<meta charset="utf-8">
<title>Full Circle Wellness – Business Card</title>
<link rel="stylesheet" href="https://fonts.googleapis.com/css2?family=Arimo:wght@400;700&display=swap">
<style>
  :root {
    --brand: #3e3d8f;
    --brand-glow: #41418e;
    --slate: #4a4a4e;
    --band: #4a4a4a;
    --paper: #fcfcfc;
    --ink: #333333;
    --white: #ffffff;
  }
  html, body {
    margin: 0;
    padding: 0;
    width: 1028px;
    height: 1200px;
    overflow: hidden;
    background: var(--white);
    font-family: "Arimo", Arial, sans-serif;
  }
  .card {
    position: absolute;
    left: 35px;
    width: 958px;
    height: 547px;
    overflow: hidden;
  }
  .card--front {
    top: 35px;
    background: radial-gradient(ellipse 520px 420px at 520px 240px, var(--brand-glow) 0%, #45457a 55%, var(--slate) 100%);
    color: var(--white);
  }
  .card--back {
    top: 617px;
    background: var(--paper);
    color: var(--ink);
  }
  .line {
    position: absolute;
    white-space: nowrap;
    line-height: 1;
    transform: translateY(-50%);
  }

  /* Front: services and hours */
  .services-heading { right: 476px; top: 114px; font-size: 35px; }
  .hours-heading { right: 492px; top: 345px; font-size: 35px; }
  .service { right: 503px; font-size: 29px; }
  .service::after {
    content: "";
    position: absolute;
    right: -20px;
    top: 50%;
    width: 7px;
    height: 7px;
    margin-top: -3px;
    border-radius: 50%;
    background: var(--white);
  }
  .clinic-statement {
    left: 0; right: 0; top: 511px;
    text-align: center;
    font-size: 29px;
  }

  /* Brand lockup */
  .brand-name { font-weight: 700; letter-spacing: -0.5px; }
  .brand-mark { position: absolute; border-radius: 50%; }
  .brand-tagline { font-size: 19px; }

  .card--front .brand-name { left: 513px; top: 245px; font-size: 38px; }
  .card--front .brand-mark { left: 542px; top: 272px; width: 52px; height: 52px; background: var(--white); }
  .card--front .brand-tagline { left: 610px; top: 290px; }

  .card--back .brand-name { left: 35px; top: 58px; font-size: 40px; color: var(--ink); }
  .card--back .brand-mark { left: 64px; top: 86px; width: 48px; height: 48px; background: var(--brand); }
  .card--back .brand-tagline { left: 131px; top: 110px; color: var(--ink); }

  /* Offer badge */
  .offer {
    position: absolute;
    left: 753px; top: 34px;
    width: 172px; height: 172px;
    border-radius: 50%;
    background: var(--brand);
    color: var(--white);
    display: flex;
    align-items: center;
    justify-content: center;
    text-align: center;
    font-size: 26px;
    line-height: 1.15;
  }

  .address { left: 35px; top: 242px; font-size: 30px; line-height: 1.15; }

  /* Contact rows */
  .icon {
    position: absolute;
    width: 51px; height: 51px;
    border-radius: 50%;
    background: var(--brand);
    display: flex;
    align-items: center;
    justify-content: center;
    transform: translateY(-50%);
  }
  .icon--right { left: 872px; }
  .icon svg { width: 30px; height: 30px; }
  .contact-text { font-size: 29px; }
  .contact-text--left { left: 120px; }
  .contact-text--right { right: 118px; text-align: right; }

  /* Footer band */
  .footer-band {
    position: absolute;
    left: 0; top: 462px;
    width: 958px; height: 85px;
    background: var(--band);
    color: var(--white);
  }
  .footer-band .line { right: 118px; font-size: 26px; text-align: right; }
  .social-dot {
    position: absolute;
    left: 872px; top: 9px;
    width: 51px; height: 51px;
    border-radius: 50%;
    background: var(--white);
  }
</style>
</head>
<body>

<section class="card card--front">
  <div class="line services-heading">Specializing in:</div>
  <div class="line service" style="top:162px">Medical, Sports Massage</div>
  <div class="line service" style="top:208px">Manual Therapies</div>
  <div class="line service" style="top:253px">Chiropractic and</div>
  <div class="line service" style="top:299px">Acupuncture</div>
  <div class="line hours-heading">Hours:</div>
  <div class="line service" style="top:386px">Monday - Friday 9 - 6</div>
  <div class="line service" style="top:432px">Saturday 10 - 6</div>

  <div class="line brand-name">Full Circle Wellness</div>
  <span class="brand-mark"></span>
  <div class="line brand-tagline">Sports Therapy and Wellness Center</div>

  <div class="line clinic-statement">We are an integrative medical clinic</div>
</section>

<section class="card card--back">
  <div class="line brand-name">Full Circle Wellness</div>
  <span class="brand-mark"></span>
  <div class="line brand-tagline">Sports Therapy and Wellness Center</div>

  <div class="offer">20% OFF<br>FIRST VISIT</div>

  <div class="line address">1480 Cerrillos Rd, Suite 4<br>Santa Fe, NM 87505</div>

  <span class="icon" style="left:35px; top:333px" aria-label="Email">
    <svg viewBox="0 0 30 30" fill="none" stroke="#fff" stroke-width="1.8"><rect x="4" y="8" width="22" height="15"/><path d="M4 8 L15 17 L26 8 M4 23 L12 15 M26 23 L18 15"/></svg>
  </span>
  <div class="line contact-text contact-text--left" style="top:333px">info@fullcirclewellnessnm.com</div>

  <span class="icon" style="left:35px; top:402px" aria-label="Website">
    <svg viewBox="0 0 30 30" fill="none" stroke="#fff" stroke-width="1.6"><circle cx="15" cy="15" r="11"/><ellipse cx="15" cy="15" rx="5" ry="11"/><path d="M4 15 H26 M6 9.5 H24 M6 20.5 H24 M15 4 V26"/></svg>
  </span>
  <div class="line contact-text contact-text--left" style="top:402px">www.fullcirclewellnessnm.com</div>

  <div class="line contact-text contact-text--right" style="top:333px">5055583927</div>
  <span class="icon icon--right" style="top:333px" aria-label="Phone">
    <svg viewBox="0 0 30 30"><path fill="#fff" d="M8 4 L12 4 L14 10 L11 12.5 C12.5 16 14 17.5 17.5 19 L20 16 L26 18 L26 22 C26 24 24 26 22 26 C13 25 5 17 4 8 C4 6 6 4 8 4 Z"/></svg>
  </span>

  <div class="line contact-text contact-text--right" style="top:402px">5055583926</div>
  <span class="icon icon--right" style="top:402px" aria-label="Fax">
    <svg viewBox="0 0 30 30" fill="none" stroke="#fff" stroke-width="2"><path d="M9 11 V4 H19 L22 7 V11"/><rect x="4" y="11" width="22" height="10" rx="2"/><rect x="9" y="17" width="12" height="9" fill="#3e3d8f"/></svg>
  </span>

  <div class="footer-band">
    <div class="line" style="top:32px">We Accept</div>
    <div class="line" style="top:62px">Some Insurances, Worker’s Company and Personal Injury.</div>
    <span class="social-dot"></span>
  </div>
</section>

</body>
</html>
```